Moon River Wellness Buisness Cards

I am looking to create a business card for a healing business. In the business I provide coaching and Reiki. I am a licensed LCPC (licensed clinical professional counselor)

Moon River Wellness
Soul Centered Healing, Reiki Healinig

Lena Vasquez, L.C.P.C

The card should include the following
biz name: Moon River Wellness
my name: Lena Vasquez
website: Lenavasquez.example
email: lena.dorwin@mailbox.example
instagram handle: lenadorwinvasquez

Target Market(s)

Women ages 25-65

```html
<!DOCTYPE html>
<html lang="en">
<head>
<meta charset="utf-8">
<title>Moon River Wellness — Business Cards</title>
<link href="https://fonts.googleapis.com/css2?family=Jost:wght@400;500;600&display=swap" rel="stylesheet">
<style>
  :root {
    --page-bg: #eeeeee;
    --card-white: #ffffff;
    --card-pink: #f4d6e6;
    --brand-ink: #3b2a36;
    --accent-magenta: #d81b7f;
    --contact-magenta: #e0399a;
  }
  html, body {
    margin: 0;
    padding: 0;
    width: 1200px;
    height: 1200px;
    overflow: hidden;
    background: var(--page-bg);
    font-family: "Jost", "Futura", sans-serif;
  }
  .canvas {
    position: relative;
    width: 1200px;
    height: 1200px;
  }
  .card {
    position: absolute;
    left: 250px;
    width: 700px;
    height: 400px;
    box-sizing: border-box;
    box-shadow: 0 6px 18px rgba(0,0,0,0.12);
  }
  .card--front {
    top: 130px;
    background: var(--card-white);
  }
  .card--back {
    top: 670px;
    background: var(--card-pink);
  }
  .brand {
    position: absolute;
    left: 60px;
    bottom: 60px;
  }
  .brand__name {
    margin: 0;
    font-weight: 500;
    font-size: 54px;
    line-height: 1.1;
    letter-spacing: 0;
    color: var(--brand-ink);
    white-space: nowrap;
  }
  .brand__tagline {
    margin: 14px 0 0 0;
    font-weight: 400;
    font-size: 18px;
    letter-spacing: 1.5px;
    text-transform: uppercase;
    color: var(--accent-magenta);
  }
  .contact {
    position: absolute;
    left: 60px;
    bottom: 60px;
  }
  .contact__name {
    margin: 0 0 12px 0;
    font-weight: 600;
    font-size: 34px;
    letter-spacing: 1.5px;
    text-transform: uppercase;
    color: var(--accent-magenta);
  }
  .contact__list {
    list-style: none;
    margin: 0;
    padding: 0;
  }
  .contact__item {
    display: flex;
    align-items: center;
    gap: 12px;
    font-size: 19px;
    line-height: 30px;
    letter-spacing: 0.3px;
    color: var(--contact-magenta);
  }
  .contact__icon {
    width: 16px;
    height: 16px;
    flex: none;
  }
</style>
</head>
<body>
<main class="canvas">
  <section class="card card--front" aria-label="Business card front">
    <div class="brand">
      <h1 class="brand__name">Moon River Wellness</h1>
      <p class="brand__tagline">Counseling · Coaching · Reiki Sessions</p>
    </div>
  </section>

  <section class="card card--back" aria-label="Business card back">
    <div class="contact">
      <h2 class="contact__name">Lena Vasquez, LCPC</h2>
      <ul class="contact__list">
        <li class="contact__item">
          <svg class="contact__icon" viewBox="0 0 16 16" aria-hidden="true">
            <circle cx="8" cy="8" r="6.5" fill="none" stroke="currentColor" stroke-width="1.4"/>
            <ellipse cx="8" cy="8" rx="2.8" ry="6.5" fill="none" stroke="currentColor" stroke-width="1.2"/>
            <line x1="1.5" y1="8" x2="14.5" y2="8" stroke="currentColor" stroke-width="1.2"/>
          </svg>
          www.lenavasquez.example
        </li>
        <li class="contact__item">
          <svg class="contact__icon" viewBox="0 0 16 16" aria-hidden="true">
            <rect x="1" y="3" width="14" height="10" fill="currentColor"/>
            <polyline points="1,3 8,9 15,3" fill="none" stroke="var(--card-pink)" stroke-width="1.3"/>
          </svg>
          lena.dorwin@mailbox.example
        </li>
        <li class="contact__item">
          <svg class="contact__icon" viewBox="0 0 16 16" aria-hidden="true">
            <circle cx="8" cy="8" r="6" fill="none" stroke="currentColor" stroke-width="1.6"/>
          </svg>
          lenadorwinvasquez
        </li>
      </ul>
    </div>
  </section>
</main>
</body>
</html>
```